Bright-loop designs Business Card

embroidery printing

Target Market(s)

Businesses and public

Industry/Entity Type

Business

Contact Information for Business Card

Front of card..... Bright-loop designs .... Corin Maltby..... 868 512-7361.... Email... bright_loopdesigns@mailbrook.net

Back of card..... Bright-loop designs embroidery & artwork

Colors
000000

```html
<!DOCTYPE html>
<html lang="en">
<head>
<meta charset="utf-8">
<title>Bright-loop designs Business Card</title>
<link href="https://fonts.googleapis.com/css2?family=Arimo:wght@400;700&family=Tinos:wght@700&display=swap" rel="stylesheet">
<style>
  :root {
    --backdrop: #e8e4dd;
    --card-white: #ffffff;
    --card-black: #0d0d0d;
    --brand-red: #9b1519;
    --brand-red-dark: #7c1013;
    --brand-gold: #d49a2a;
    --text-light: #ffffff;
    --text-grey: #bdbdbd;
  }
  * { margin: 0; padding: 0; box-sizing: border-box; }
  html, body { width: 1200px; height: 892px; overflow: hidden; }
  body {
    background: var(--backdrop);
    font-family: "Arimo", Arial, sans-serif;
    position: relative;
  }
  .card {
    position: absolute;
    left: 320px;
    width: 560px;
    height: 320px;
    overflow: hidden;
    box-shadow: 0 6px 18px rgba(0,0,0,0.18);
  }
  .card-front { top: 70px; background: var(--card-white); }
  .card-back { top: 500px; background: var(--card-black); }

  .front-waves { position: absolute; inset: 0; }

  .front-logo {
    position: absolute;
    top: 34px;
    right: 40px;
    font-weight: 700;
    font-size: 34px;
    color: var(--brand-red);
    letter-spacing: 1px;
  }

  .holder { position: absolute; left: 28px; top: 128px; color: var(--text-light); }
  .holder-name { font-family: "Tinos", "Times New Roman", serif; font-weight: 700; font-size: 26px; }
  .holder-title { font-size: 14px; margin-top: 4px; }

  .contact-list {
    position: absolute;
    right: 18px;
    bottom: 20px;
    list-style: none;
    color: var(--text-light);
    font-size: 14px;
  }
  .contact-list li { display: flex; justify-content: flex-end; align-items: center; gap: 8px; line-height: 22px; }
  .contact-icon { width: 15px; height: 15px; flex: none; }

  .back-logo {
    position: absolute;
    top: 84px;
    width: 100%;
    text-align: center;
    font-weight: 700;
    font-size: 44px;
    color: var(--brand-red);
    letter-spacing: 1px;
  }
  .back-tagline {
    position: absolute;
    top: 146px;
    width: 100%;
    text-align: center;
    font-size: 16px;
    letter-spacing: 3px;
    text-transform: uppercase;
    color: var(--text-grey);
  }
  .back-web {
    position: absolute;
    top: 210px;
    left: 0;
    width: 100%;
    display: flex;
    align-items: center;
    justify-content: center;
    gap: 14px;
    color: var(--text-light);
    font-size: 22px;
  }
  .back-rule { width: 110px; height: 1px; background: var(--text-grey); }
</style>
</head>
<body>

  <section class="card card-front" aria-label="Business card front">
    <svg class="front-waves" width="560" height="320" viewBox="0 0 560 320" aria-hidden="true">
      <defs>
        <linearGradient id="red-shade" x1="0" y1="0" x2="1" y2="1">
          <stop offset="0" stop-color="var(--brand-red)"/>
          <stop offset="1" stop-color="var(--brand-red-dark)"/>
        </linearGradient>
      </defs>
      <path d="M0,62 C140,52 230,112 320,142 C410,170 500,162 560,140 L560,320 L0,320 Z" fill="var(--brand-gold)"/>
      <path d="M0,76 C140,66 230,126 320,156 C410,184 500,176 560,154 L560,320 L0,320 Z" fill="var(--card-white)"/>
      <path d="M0,82 C140,72 230,132 320,162 C410,190 500,182 560,160 L560,320 L0,320 Z" fill="url(#red-shade)"/>
    </svg>

    <div class="front-logo">Bright-loop designs</div>

    <div class="holder">
      <div class="holder-name">Corin Maltby</div>
      <div class="holder-title">Managing Director</div>
    </div>

    <ul class="contact-list">
      <li>868 512-7361
        <svg class="contact-icon" viewBox="0 0 16 16" aria-hidden="true"><rect width="16" height="16" fill="#fff"/><path d="M4 3h3l1 3-2 1c1 2 2 3 3 3l1-2 3 1v3c-6 1-10-3-9-9z" fill="var(--brand-red)"/></svg></li>
      <li>www.brightloopdesigns.com
        <svg class="contact-icon" viewBox="0 0 16 16" aria-hidden="true"><rect width="16" height="16" fill="#fff"/><circle cx="8" cy="8" r="5" fill="none" stroke="var(--brand-red)" stroke-width="1.5"/><path d="M3 8h10M8 3v10" stroke="var(--brand-red)" stroke-width="1.2"/></svg></li>
      <li>bright_loopdesigns@mailbrook.net
        <svg class="contact-icon" viewBox="0 0 16 16" aria-hidden="true"><rect width="16" height="16" fill="#fff"/><rect x="3" y="5" width="10" height="7" fill="var(--brand-red)"/><path d="M3 5l5 4 5-4" fill="none" stroke="#fff" stroke-width="1"/></svg></li>
      <li>Fenmore Road, London, United Kingdom
        <svg class="contact-icon" viewBox="0 0 16 16" aria-hidden="true"><rect width="16" height="16" fill="#fff"/><path d="M8 3l5 5h-2v5H5V8H3z" fill="var(--brand-red)"/></svg></li>
    </ul>
  </section>

  <section class="card card-back" aria-label="Business card back">
    <div class="back-logo">Bright-loop designs</div>
    <div class="back-tagline">embroidery &amp; artwork</div>
    <div class="back-web">
      <span class="back-rule"></span>
      <span>www.brightloopdesigns.com</span>
      <span class="back-rule"></span>
    </div>
  </section>

</body>
</html>
```